Diversity report of banking market in Europe

*Power point presentation style - rather than corporate brochure*
We are an executive recruitment firm who will be sending a report to all our senior clients. We need a designer to make it look eye catching, slick and professional for our audience. The document will be read mainly by PDF so the type of font and size will be very important as will the size of each page.

We have all the content but may need guidance on the amount of text, the size of graphs and inserting some pictures/vectors etc. We can provide more text or cut text back it it helps the design. We can find more graphs if this helps to fill a page

Industry/Entity Type

Investment Banking

Font styles to use
Sans Serif

Colors
0255a3
33b8a4
85cae6
cfeae6
ffffff

Requirements
Must have
• Colours:
11, 29, 49
70, 165, 175
Nice to have
• Have added two example Varnholt documents that we feel are clean and professional. Please use these are our attempt as a guide line to how was want the document to look and feel and flow. Happy to add additional pictures or design to fill out pages. Cant steal actual pictures from varnholt report

```html
<!DOCTYPE html>
<html lang="en">
<head>
<meta charset="utf-8">
<title>Gender Diversity by Seniority</title>
<link href="https://fonts.googleapis.com/css2?family=Montserrat:ital,wght@0,400;0,500;0,600;0,700;0,800;1,700;1,800&display=swap" rel="stylesheet">
<style>
  :root{
    --navy:#0b1d31;
    --teal:#46a5af;
    --teal-bright:#1aa6b4;
    --teal-soft:#7fc4cc;
    --sky:#d7ecf2;
    --ink:#1c2a38;
    --white:#ffffff;
  }
  *{margin:0;padding:0;box-sizing:border-box}
  html,body{width:1200px;height:675px;overflow:hidden;background:var(--white)}
  body{font-family:"Montserrat",Arial,sans-serif;color:var(--ink);position:relative}

  .chart{position:absolute;left:44px;top:38px;width:330px}
  .chart-title{font-size:10px;font-weight:500;color:var(--ink)}
  .legend{position:absolute;right:0;top:20px;display:flex;gap:12px;font-size:9px}
  .legend span{display:flex;align-items:center;gap:4px}
  .legend i{display:inline-block;width:8px;height:8px}
  .level{position:absolute;left:0;font-size:10px;font-weight:700;text-transform:uppercase}
  .bar{position:absolute;left:0;width:326px;height:31px;display:flex;font-size:9px;color:var(--white)}
  .bar .male{background:var(--navy);display:flex;align-items:center;justify-content:center}
  .bar .female{background:var(--teal-bright);display:flex;align-items:center;justify-content:center;color:var(--navy)}

  .stat{position:absolute;border-radius:50%;color:var(--white);text-align:center;display:flex;flex-direction:column;justify-content:center;align-items:center}
  .stat b{font-size:34px;font-weight:700;line-height:1}
  .stat small{font-size:10.5px;line-height:1.25;margin-top:8px}
  .stat-overall{left:413px;top:73px;width:154px;height:154px;background:var(--teal)}
  .stat-senior{left:585px;top:73px;width:154px;height:154px;background:var(--teal-soft)}

  .kicker{position:absolute;right:40px;top:40px;font-size:17px;color:var(--teal);font-weight:500}
  .headline{position:absolute;right:40px;top:66px;text-align:right;color:var(--teal);font-weight:800;font-size:52px;line-height:58px;letter-spacing:-1.5px}

  .pyramid{position:absolute;left:40px;top:238px;width:204px;height:350px}
  .tier-label{position:absolute;width:204px;text-align:center;color:var(--teal);font-size:8px;font-weight:600}
  .tier-label strong{display:block;font-size:13px;color:var(--navy);font-weight:700}
  .ratio-title{position:absolute;left:28px;top:596px;width:240px;font-size:13px;font-weight:800;color:var(--navy);line-height:1.2}

  .copy{position:absolute;left:254px;top:262px;width:906px;text-align:right;font-size:9.3px;line-height:1.5;color:var(--ink)}
  .copy p{margin-bottom:11px}
  .copy p.tight{margin-bottom:4px}
  .callout{color:var(--teal);font-style:italic;font-weight:800;font-size:14px;line-height:1.3}
  .callout em{font-size:19px;font-style:italic}
  .callout-wrap{margin-bottom:4px}

  .folio{position:absolute;top:645px;font-size:8px;color:var(--ink)}
  .folio-left{left:34px}
  .folio-right{right:20px}
</style>
</head>
<body>

<section class="chart">
  <p class="chart-title">% Split of all males to females across all strategies, by level</p>
  <div class="legend">
    <span><i style="background:var(--navy)"></i>Male</span>
    <span><i style="background:var(--teal-bright)"></i>Female</span>
  </div>
  <div class="level" style="top:28px">Senior</div>
  <div class="bar" style="top:43px"><div class="male" style="width:92.6%">92.6%</div><div class="female" style="width:7.4%">7.4%</div></div>
  <div class="level" style="top:84px">Mid Level</div>
  <div class="bar" style="top:99px"><div class="male" style="width:82.7%">82.7%</div><div class="female" style="width:17.3%">17.3%</div></div>
  <div class="level" style="top:140px">Junior</div>
  <div class="bar" style="top:155px"><div class="male" style="width:75.6%">75.6%</div><div class="female" style="width:24.4%">24.4%</div></div>
</section>

<div class="stat stat-overall"><b>14%</b><small>Percentage of<br>females overall</small></div>
<div class="stat stat-senior"><b>7.4%</b><small>Percentage of<br>females holding a<br>senior position</small></div>

<p class="kicker">Diversity &amp; Inclusion</p>
<h1 class="headline">GENDER<br>DIVERSITY<br>BY SENIORITY</h1>

<svg class="pyramid" viewBox="0 0 204 350" aria-hidden="true">
  <polygon points="102,0 204,350 0,350" fill="var(--sky)"/>
</svg>
<svg style="position:absolute;left:88px;top:272px" width="110" height="72" role="img" aria-label="Icon grid: one female to every 13.5 male professionals at senior level">
  <rect x="0" y="0" width="110" height="72" rx="4" fill="var(--navy)" opacity=".75"/>
</svg>
<div class="tier-label" style="left:40px;top:355px">Senior Level:<strong>1 to every 13.5</strong></div>
<svg style="position:absolute;left:94px;top:420px" width="92" height="38" role="img" aria-label="Icon row: one female to every 5 male professionals at mid level">
  <rect x="0" y="0" width="92" height="38" rx="4" fill="var(--navy)" opacity=".75"/>
</svg>
<div class="tier-label" style="left:40px;top:462px">Mid-Level:<strong>1 to every 5</strong></div>
<svg style="position:absolute;left:110px;top:530px" width="72" height="30" role="img" aria-label="Icon row: one female to every 3 male professionals at junior level">
  <rect x="0" y="0" width="72" height="30" rx="4" fill="var(--navy)" opacity=".75"/>
</svg>
<div class="tier-label" style="left:40px;top:564px">Junior Level:<strong>1 to every 3</strong></div>
<p class="ratio-title">RATIO OF FEMALE TO MALE<br>PROFESSIONALS</p>

<article class="copy">
  <p class="tight">Men dominate the figures of investment professionals working in the European Corporate Credit markets that we've analysed in this report. Nowhere is this more prevalent than at a senior level within these firms, where females account for just 7.4% of senior positions which is only 2.9% of the entire workforce we reviewed.</p>
  <div class="callout-wrap">
    <p class="callout">There are <em>163</em> Senior females working across these strategies</p>
    <p class="callout">There are <em>2036</em> Senior males working across these strategies</p>
  </div>
  <p>Of all 5714 professionals working across these strategies there are 2,199 senior team members and women only account for 7.4% of these which is the biggest gap of all three levels. At mid-level women account for 17.3% of mid-level professionals. At junior level women account for 24.4%.</p>
  <p>A report produced by Fairmont Invest found that 17% of accountants across the UK at Partner level are female. Across all seniorities the total level of gender diversity in chartered accountancy is far higher than we witness in Investment Banking and specifically the corporate credit markets Ashdown Reeve specialises in. Across chartered accountancy, females account for 45% of the work force. What pressures, resistance, choices, factors account for the 28% drop in female representation at a senior level in the chartered accountancy sector. I could only speculate, as anyone could faced with justifying the drop. As a woman, and a mum, and a professional, I think there will be several combined factors that may account for this drop. I'm sure some may review these statistics and conclude that there is systemic patriarchy and male privilege at play. I've questioned my thinking many times over, should I as a woman who strongly believes in equality point to these numbers and feel they represent male dominance through privilege, or are the female individuals joining and leaving the non-investment grade Corporate Credit markets at higher rates than accountancy for other reasons.</p>
  <p>Are the demands and stresses faced in banking unappealing to women at a certain level, do women reach a point in their career in banking where the working hours are simply too much to handle whilst bringing up a family? Is the demographic of senior female professionals in Corporate credit weighted with career women who chose not to raise children? Are the women who are attracted to the finance industry fundamentally different characteristically from the females who enter accountancy? Have the women who set out on this career path done so for different reasons than the females that join other mathematically based careers?</p>
  <p>So many questions, and I'm afraid very difficult questions to answer. Do all these questions play a part in these figures, or are women underrepresented in senior management because they are not given the opportunity to progress and are held back by a system that favours men over women. I am as intrigued as anyone to know the answer, as I am unable to provide one, I will provide more information so that you can draw your own conclusions</p>
</article>

<p class="folio folio-left">05 &nbsp; © Ashdown Reeve</p>
<p class="folio folio-right">© Ashdown Reeve &nbsp; 06</p>

</body>
</html>
```